Business Cards and Stationary for a new consulting, recruiting and outsourcing company in Germany
BRAUNFELD Consulting
Business Cards and Stationary for a new consulting, recruiting and outsourcing company in Germany  - Consulting
Creative Brief
Professional
BRAUNFELD Consulting (Company Name) Ramune Braunfeld (First name, last name)
Inhaberin ("Owner" for english version)
Im Lindgrund 5 89512 Tannbach Deutschland ("Germany" for english version)
ramune.braunfeld@braunfeld-beratung.example
htttps://www.braunfeld-beratung.example
The round logo version with black background size around 75% of the card.

```html
<!DOCTYPE html>
<html lang="en">
<head>
<meta charset="utf-8">
<title>BRAUNFELD Consulting – Stationery</title>
<link href="https://fonts.googleapis.com/css2?family=Questrial&display=swap" rel="stylesheet">
<style>
:root{
  --bg:#dcdcdc;
  --paper:#ffffff;
  --blue:#29a9e1;
  --orange:#f7941d;
  --ink:#3a3a3a;
  --muted:#7a7a7a;
  --faint:#e3f1f9;
  --black:#111111;
}
*{margin:0;padding:0;box-sizing:border-box}
html,body{width:1200px;height:936px;overflow:hidden;background:var(--bg)}
body{position:relative;font-family:"Questrial",Arial,sans-serif;color:var(--ink)}
.sheet{position:absolute;background:var(--paper);overflow:hidden}
.wave{position:absolute;left:0;bottom:0;width:100%}
.brand{position:absolute;display:flex;align-items:center;gap:8px;white-space:nowrap;color:var(--ink)}
.brand-dot{border-radius:50%;background:var(--blue);flex:none}
.faint-disc{position:absolute;border-radius:50%;background:var(--faint)}

/* letterhead */
.letterhead{left:144px;top:66px;width:426px;height:542px}
.letterhead .brand{left:38px;top:34px;font-size:15px}
.letterhead .brand-dot{width:22px;height:22px}
.letter-contact{position:absolute;right:22px;top:30px;font-size:5.5px;line-height:8px;text-align:right;color:var(--muted)}
.letter-body{position:absolute;left:38px;top:120px;width:340px;font-size:6px;line-height:9px;color:var(--muted)}
.letter-body p{margin-bottom:9px}
.letterhead .faint-disc{width:110px;height:110px;right:36px;bottom:60px}

/* folder */
.folder{left:628px;top:46px;width:438px;height:562px}
.folder .brand{left:90px;top:235px;font-size:22px}
.folder .brand-dot{width:40px;height:40px}
.folder .faint-disc{width:220px;height:220px;right:20px;bottom:70px}

/* business cards */
.card-front{left:38px;top:663px;width:210px;height:102px}
.card-front .brand{left:14px;top:12px;font-size:9px}
.card-front .brand-dot{width:13px;height:13px}
.card-details{position:absolute;left:14px;top:40px;font-size:5px;line-height:7px;color:var(--muted)}
.card-details strong{font-weight:400;color:var(--ink);font-size:6px}
.card-back{left:38px;top:793px;width:210px;height:98px;background:var(--black)}
.card-back .brand{left:50%;top:50%;transform:translate(-50%,-50%);flex-direction:column;gap:6px;font-size:9px;color:#fff}
.card-back .brand-dot{width:40px;height:40px}

/* envelopes */
.envelope{left:266px;top:679px;width:380px;height:200px}
.envelope .brand{left:18px;top:18px;font-size:15px}
.envelope .brand-dot{width:22px;height:22px}
.envelope .faint-disc{width:100px;height:100px;left:140px;top:20px}
.envelope-back{left:666px;top:679px;width:499px;height:207px}
.flap-band{position:absolute;left:0;top:0;width:100%;height:40px;background:var(--blue);color:#fff;font-size:11px;letter-spacing:1px;text-align:center;line-height:40px}
.flap-lines{position:absolute;left:0;top:40px;width:100%;height:167px}
</style>
</head>
<body>

<!-- Letterhead -->
<section class="sheet letterhead">
  <div class="brand"><span class="brand-dot"></span>BRAUNFELD Consulting</div>
  <address class="letter-contact" style="font-style:normal">
    Ramune Braunfeld<br>Im Lindgrund 5<br>89512 Tannbach<br>Deutschland<br>ramune.braunfeld@braunfeld-beratung.example<br>htttps://www.braunfeld-beratung.example
  </address>
  <div class="letter-body">
    <p>12 May 2025</p>
    <p>Jonas Keller<br>Hafenweg 3, 20457 Hamburg</p>
    <p>Dear Sir,</p>
    <p>Thank you for your interest in our consulting services. We support growing companies with recruiting, interim staffing and outsourcing solutions across Germany. Our team combines deep industry knowledge with a personal approach, so every project starts with a clear understanding of your goals and ends with measurable results for your business.</p>
    <p>In a first meeting we analyse your current structure and define the roles you need. We then search, select and present qualified candidates within an agreed time frame and accompany the onboarding.</p>
    <p>We would be pleased to discuss your requirements in person. Please contact us at any time to arrange an appointment that suits your schedule, and we will prepare a tailored proposal for you.</p>
    <p>Kind regards</p>
    <p style="margin-top:22px">Ramune Braunfeld<br>Inhaberin</p>
  </div>
  <div class="faint-disc"></div>
  <svg class="wave" viewBox="0 0 400 60" height="60" preserveAspectRatio="none">
    <path d="M0 34 C120 4 260 64 400 22 L400 60 L0 60Z" fill="var(--blue)"/>
    <path d="M0 26 C120 -6 260 54 400 12 L400 20 C260 62 120 2 0 32Z" fill="var(--orange)"/>
  </svg>
</section>

<!-- Presentation folder -->
<section class="sheet folder">
  <div class="faint-disc"></div>
  <div class="brand"><span class="brand-dot"></span>BRAUNFELD Consulting</div>
  <svg class="wave" viewBox="0 0 400 70" height="70" preserveAspectRatio="none">
    <path d="M0 40 C120 6 260 72 400 24 L400 70 L0 70Z" fill="var(--blue)"/>
    <path d="M0 30 C120 -6 260 62 400 12 L400 22 C260 70 120 4 0 38Z" fill="var(--orange)"/>
  </svg>
</section>

<!-- Business card front -->
<section class="sheet card-front">
  <div class="brand"><span class="brand-dot"></span>BRAUNFELD Consulting</div>
  <div class="card-details">
    <strong>Ramune Braunfeld</strong><br>Inhaberin<br>Im Lindgrund 5, 89512 Tannbach<br>ramune.braunfeld@braunfeld-beratung.example
  </div>
  <svg class="wave" viewBox="0 0 400 60" height="22" preserveAspectRatio="none">
    <path d="M0 34 C120 4 260 64 400 22 L400 60 L0 60Z" fill="var(--blue)"/>
    <path d="M0 26 C120 -6 260 54 400 12 L400 20 C260 62 120 2 0 32Z" fill="var(--orange)"/>
  </svg>
</section>

<!-- Business card back -->
<section class="sheet card-back">
  <div class="brand"><span class="brand-dot"></span>BRAUNFELD Consulting</div>
</section>

<!-- Envelope front -->
<section class="sheet envelope">
  <div class="faint-disc"></div>
  <div class="brand"><span class="brand-dot"></span>BRAUNFELD Consulting</div>
  <svg class="wave" viewBox="0 0 400 60" height="46" preserveAspectRatio="none">
    <path d="M0 34 C120 4 260 64 400 22 L400 60 L0 60Z" fill="var(--blue)"/>
    <path d="M0 26 C120 -6 260 54 400 12 L400 20 C260 62 120 2 0 32Z" fill="var(--orange)"/>
  </svg>
</section>

<!-- Envelope back -->
<section class="sheet envelope-back">
  <div class="flap-band">www.braunfeld-beratung.example</div>
  <svg class="flap-lines" viewBox="0 0 499 167" preserveAspectRatio="none">
    <path d="M0 0 L230 95 L269 95 L499 0" fill="none" stroke="#e6e6e6" stroke-width="1.5"/>
    <path d="M0 167 L230 95 M269 95 L499 167" fill="none" stroke="#ececec" stroke-width="1"/>
  </svg>
</section>

</body>
</html>
```